Weightloss company needs Business Card

We want a business card that is clean and professional, yet portrays that we are a friendly, innovative, and versatile program designed to fit the needs of our clients.
I would like there to be 2 sides, one side having an appointment card, and the other side containing the logo and business information. There can be decorations on both sides. The logo is attached.

Target Market(s)

Men and women 40-60

Industry/Entity Type

Business

Contact Information for Business Card

Font styles to use
Sans Serif

Requirements
Must have
• The logo, space for business information
Nice to have
• The colors in the logo
Should not have
• No pictures of people or food

```html
<!DOCTYPE html>
<html lang="en">
<head>
<meta charset="utf-8">
<title>Summit Shift – Business Card</title>
<link rel="stylesheet" href="https://fonts.googleapis.com/css2?family=Source+Sans+3:ital,wght@0,400;0,600;0,700;1,400&display=swap">
<style>
  :root {
    --backdrop: #ecebe8;
    --card-cyan: #22d8ff;
    --card-white: #ffffff;
    --brand-red: #e8173a;
    --disc-front: #eef2f3;
    --disc-back: #ededed;
    --ink: #1a1a1a;
    --text-white: #ffffff;
  }
  * { box-sizing: border-box; margin: 0; padding: 0; }
  html, body { width: 1200px; height: 900px; overflow: hidden; }
  body {
    background: var(--backdrop);
    font-family: "Source Sans 3", "Segoe UI", sans-serif;
    position: relative;
  }
  .card {
    position: absolute;
    overflow: hidden;
    box-shadow: 0 6px 18px rgba(0,0,0,0.18);
  }
  .card--front { left: 238px; top: 60px; width: 555px; height: 345px; background: var(--card-cyan); }
  .card--back  { left: 457px; top: 518px; width: 560px; height: 344px; background: var(--card-white); }

  .disc { position: absolute; border-radius: 50%; width: 300px; height: 300px; }
  .card--front .disc { left: -8px; top: 18px; background: var(--disc-front); }
  .card--back .disc { left: 272px; top: 20px; background: var(--disc-back); }

  .brand {
    position: absolute; left: 22px; top: 150px;
    display: flex; align-items: center; gap: 8px;
    color: var(--brand-red); font-weight: 700; font-size: 27px; line-height: 1;
  }
  .brand__dot { width: 14px; height: 14px; border-radius: 50%; background: var(--brand-red); }

  .person { position: absolute; right: 25px; top: 52px; text-align: right; color: var(--text-white); }
  .person__name { font-size: 21px; font-weight: 700; line-height: 1.2; }
  .person__role { font-size: 16px; font-weight: 400; line-height: 1.3; }

  .contacts { position: absolute; right: 24px; top: 199px; list-style: none; color: var(--text-white); font-size: 15px; }
  .contacts li { display: flex; justify-content: flex-end; align-items: center; gap: 8px; height: 20px; }
  .contacts svg { width: 11px; height: 11px; fill: var(--text-white); }

  .address { position: absolute; right: 25px; top: 275px; text-align: right; color: var(--text-white); font-size: 15px; line-height: 20px; font-style: normal; }

  .appointment { position: absolute; left: 32px; top: 44px; color: var(--brand-red); }
  .appointment__title { font-size: 21px; font-weight: 700; margin-bottom: 26px; }
  .field { display: flex; align-items: baseline; font-size: 14px; font-weight: 700; height: 52px; }
  .field__line { display: inline-block; width: 168px; border-bottom: 2px dotted var(--ink); margin-left: 4px; }
  .appointment__note { font-size: 15px; font-style: italic; line-height: 22px; margin-top: -8px; }
</style>
</head>
<body>
  <section class="card card--front" aria-label="Business card front">
    <div class="disc"></div>
    <div class="brand"><span class="brand__name">Summit Shift</span><span class="brand__dot"></span></div>
    <div class="person">
      <p class="person__name">Daniel Harper</p>
      <p class="person__role">Managing Director</p>
    </div>
    <ul class="contacts">
      <li>055-987 654 321
        <svg viewBox="0 0 24 24"><path d="M6.6 10.8a15 15 0 0 0 6.6 6.6l2.2-2.2c.3-.3.7-.4 1-.2 1.1.4 2.3.6 3.6.6.6 0 1 .4 1 1V20c0 .6-.4 1-1 1A17 17 0 0 1 3 4c0-.6.4-1 1-1h3.5c.6 0 1 .4 1 1 0 1.3.2 2.5.6 3.6.1.3 0 .7-.2 1z"/></svg></li>
      <li>hello@summitshift.com
        <svg viewBox="0 0 24 24"><path d="M2 5h20v14H2z M4 7v1l8 5 8-5V7l-8 5z" fill-rule="evenodd"/></svg></li>
      <li>www.summitshift.com
        <svg viewBox="0 0 24 24"><circle cx="12" cy="12" r="10"/></svg></li>
    </ul>
    <address class="address">48 Meadow Lane, Brookfield<br>Valley, 204518.</address>
  </section>

  <section class="card card--back" aria-label="Appointment card">
    <div class="disc"></div>
    <div class="appointment">
      <h2 class="appointment__title">Your Next Appointment is</h2>
      <p class="field">Name: <span class="field__line"></span></p>
      <p class="field">Date: <span class="field__line"></span></p>
      <p class="field">Time: <span class="field__line"></span></p>
      <p class="appointment__note">If unable to keep appointment,<br>kindly give 24hrs notice.</p>
    </div>
  </section>
</body>
</html>
```